Flyer-Design für Heizungsbau
Zielgruppe
Wir sind ein junges, kompetentes und zertifiziertes Fachbetrieb und bieten Beratung, Fachplanung und fachmännische Installation von Wärmepumpen, Klimaanlagen und Lüftungsanlagen. Unsere Zielgruppe sind Eigentümer von Bestandsgebäuden oder Neubauten (hauptsächlich Privatkunden in mittlerem oder höherem Alter), welche eine Heizungssanierung für Heizkostenreduzierung oder neue Heizinstallation (Wärmepumpen), und/oder mehr Komfort bzw. Luftqualität in ihren Zuhause wünschen (Klima und Lüftung).
Aufgabenstellung
Schwerpunkte: 1. Ersparnis an Heizkosten, 2. Wohlgefühl und 3. Klimaschutz

```html
<!DOCTYPE html>
<html lang="de">
<head>
<meta charset="utf-8">
<title>Frostwerk – Flyer Heizungsbau</title>
<link href="https://fonts.googleapis.com/css2?family=Roboto:wght@400;500;700;900&display=swap" rel="stylesheet">
<style>
  :root{
    --bg:#f3f3f3;
    --paper:#ffffff;
    --navy:#0f5a9c;
    --blue:#1c7cc5;
    --sky:#4daee9;
    --pale:#e8f2fb;
    --ink:#1d2b3a;
    --photo-a:#dfe4ea;
    --photo-b:#a9b9cc;
  }
  *{box-sizing:border-box;margin:0;padding:0}
  html,body{width:1200px;height:817px;overflow:hidden;background:var(--bg);font-family:"Roboto",sans-serif;color:var(--ink)}
  .stage{position:relative;width:1200px;height:817px}
  .flyer{position:absolute;top:108px;width:290px;height:600px;background:var(--paper);overflow:hidden;box-shadow:0 6px 22px rgba(0,0,0,.14)}
  .flyer--back{left:292px}
  .flyer--front{left:618px}

  /* back side */
  .hero-photo{position:absolute;left:0;top:0;width:290px;height:200px;background:linear-gradient(135deg,var(--photo-a),var(--photo-b) 70%,#3a5f9a)}
  .hero-curve{position:absolute;left:0;top:0}
  .cert-badge{position:absolute;left:22px;top:62px;width:104px;height:104px;border-radius:50%;background:var(--navy);border:4px solid #fff;box-shadow:0 3px 10px rgba(0,0,0,.25)}
  .features{position:absolute;left:18px;top:212px;right:10px}
  .feature{display:flex;gap:12px;margin-bottom:16px}
  .feature__icon{flex:0 0 34px;height:34px;margin-top:10px}
  .feature__title{font-weight:700;font-size:15px;color:var(--navy);line-height:1.15}
  .feature__text{font-size:10.5px;line-height:1.35;color:var(--ink)}
  .contact{position:absolute;left:0;top:455px;width:290px;height:145px}
  .contact__bg{position:absolute;left:0;top:0}
  .contact__body{position:absolute;left:28px;top:26px;right:12px}
  .contact__head{font-weight:700;font-size:16px;line-height:1.15;color:var(--navy)}
  .contact__phone{display:flex;align-items:center;gap:6px;margin-top:6px;font-weight:700;font-size:17px;color:var(--sky)}
  .contact__web{font-size:10px;margin-top:4px}
  .band{position:absolute;left:0;bottom:0;width:290px;height:36px;background:var(--navy);color:#fff;font-weight:700;font-size:15px;display:flex;align-items:center;justify-content:center}

  /* front side */
  .brand{position:absolute;left:0;right:0;top:30px;display:flex;align-items:center;justify-content:center;gap:12px}
  .brand__dot{width:30px;height:30px;border-radius:50%;background:var(--navy)}
  .brand__name{font-weight:500;font-size:32px;color:var(--sky);letter-spacing:.5px}
  .kicker{position:absolute;top:96px;left:0;right:0;text-align:center;font-size:16px;color:var(--sky)}
  .headline{position:absolute;top:118px;left:0;right:0;text-align:center;font-weight:900;font-size:24px;line-height:1.18;color:var(--navy)}
  .rule{position:absolute;top:192px;left:124px;width:42px;height:3px;background:var(--sky)}
  .front-photo{position:absolute;left:0;top:208px;width:290px;height:210px;background:linear-gradient(160deg,#f6f8fa,#dde4ec 55%,#9fb1c8)}
  .about{position:absolute;left:0;top:380px}
  .about__body{position:absolute;left:20px;top:416px;right:14px;color:#fff}
  .about__title{font-weight:700;font-size:19px}
  .about__text{font-size:9.5px;line-height:1.5;margin-top:6px}
  .about__text b{font-weight:700}
  .services{font-weight:700;font-size:16px;margin-top:10px;white-space:nowrap}
  .band--front{background:#155c9e;height:40px}
</style>
</head>
<body>
<main class="stage">

  <!-- Back side -->
  <section class="flyer flyer--back">
    <div class="hero-photo" role="img" aria-label="Foto: Monteur installiert Verteilerleitungen an einer Wand"></div>
    <svg class="hero-curve" width="290" height="215" viewBox="0 0 290 215" aria-hidden="true">
      <path d="M0,215 L0,195 Q160,190 290,125 L290,215 Z" fill="#fff"/>
      <path d="M0,200 Q160,192 290,128 L290,140 Q160,202 0,210 Z" fill="var(--blue)"/>
    </svg>
    <div class="cert-badge" role="img" aria-label="Zertifikatssiegel"></div>

    <div class="features">
      <div class="feature">
        <svg class="feature__icon" viewBox="0 0 34 34" aria-hidden="true"><circle cx="17" cy="17" r="14" fill="none" stroke="var(--navy)" stroke-width="3.5"/><path d="M17 9v9l6 3" fill="none" stroke="var(--navy)" stroke-width="3.5" stroke-linecap="round"/></svg>
        <div><h3 class="feature__title">Schnelle Installation</h3><p class="feature__text">Garantierte Installation Ihrer Klimaanlage innerhalb von wenigen Wochen</p></div>
      </div>
      <div class="feature">
        <svg class="feature__icon" viewBox="0 0 34 34" aria-hidden="true"><rect x="2" y="6" width="30" height="22" rx="3" fill="none" stroke="var(--navy)" stroke-width="3.5"/><rect x="2" y="11" width="30" height="4" fill="var(--navy)"/><rect x="7" y="20" width="8" height="3" fill="var(--navy)"/></svg>
        <div><h3 class="feature__title">Fair Preise</h3><p class="feature__text">Alle unsere Angebote sind zum Festpreis und ändern sich durch mehr Aufwand auch nicht</p></div>
      </div>
      <div class="feature">
        <svg class="feature__icon" viewBox="0 0 34 34" aria-hidden="true"><circle cx="17" cy="17" r="14" fill="none" stroke="var(--navy)" stroke-width="3.5"/><path d="M10 17l5 5 9-10" fill="none" stroke="var(--navy)" stroke-width="3.5" stroke-linecap="round" stroke-linejoin="round"/></svg>
        <div><h3 class="feature__title">Höchste Qualität</h3><p class="feature__text">Wir führen jede Arbeit mit höchster Sorgfalt und Qualität durch</p></div>
      </div>
      <div class="feature">
        <svg class="feature__icon" viewBox="0 0 34 34" aria-hidden="true"><rect x="2" y="9" width="30" height="16" rx="2" fill="var(--navy)"/><circle cx="17" cy="17" r="4.5" fill="#fff"/><circle cx="7" cy="17" r="1.6" fill="#fff"/><circle cx="27" cy="17" r="1.6" fill="#fff"/></svg>
        <div><h3 class="feature__title">Festpreise</h3><p class="feature__text">Wir sind von fairen Preisen überzeugt und bieten ein faires Preis-/Leistungsverhältnis</p></div>
      </div>
    </div>

    <div class="contact">
      <svg class="contact__bg" width="290" height="145" viewBox="0 0 290 145" aria-hidden="true">
        <defs><linearGradient id="paleFade" x1="0" y1="0" x2="0" y2="1"><stop offset="0" stop-color="#f4f9fd"/><stop offset="1" stop-color="var(--pale)"/></linearGradient></defs>
        <path d="M0,10 Q150,16 290,0 L290,145 L0,145 Z" fill="url(#paleFade)"/>
      </svg>
      <div class="contact__body">
        <p class="contact__head">Sie haben noch Fragen?<br>Rufen Sie uns an:</p>
        <p class="contact__phone">
          <svg width="16" height="16" viewBox="0 0 24 24" aria-hidden="true"><path d="M6.6 10.8a15 15 0 0 0 6.6 6.6l2.2-2.2a1 1 0 0 1 1-.25 11 11 0 0 0 3.6.6 1 1 0 0 1 1 1V20a1 1 0 0 1-1 1A17 17 0 0 1 3 4a1 1 0 0 1 1-1h3.5a1 1 0 0 1 1 1c0 1.25.2 2.45.6 3.6a1 1 0 0 1-.25 1z" fill="var(--sky)"/></svg>
          06841/5520374
        </p>
        <p class="contact__web">Oder besuchen Sie unsere Website:</p>
      </div>
    </div>
    <div class="band">frostwerk-klima.de</div>
  </section>

  <!-- Front side -->
  <section class="flyer flyer--front">
    <div class="brand"><span class="brand__dot"></span><span class="brand__name">Frostwerk</span></div>
    <p class="kicker">Jetzt einbauen!</p>
    <h1 class="headline">Heizkosten sparen,<br>glücklich leben!</h1>
    <div class="rule"></div>
    <div class="front-photo" role="img" aria-label="Foto: lächelnder Monteur mit Klimagerät und Wärmepumpe"></div>
    <svg class="about" width="290" height="220" viewBox="0 0 290 220" aria-hidden="true">
      <defs><linearGradient id="aboutBlue" x1="0" y1="0" x2="0" y2="1"><stop offset="0" stop-color="var(--blue)"/><stop offset="1" stop-color="#1f86d0"/></linearGradient></defs>
      <path d="M0,0 Q120,24 290,24 L290,220 L0,220 Z" fill="var(--sky)"/>
      <path d="M0,10 Q120,36 290,34 L290,220 L0,220 Z" fill="url(#aboutBlue)"/>
    </svg>
    <div class="about__body">
      <h2 class="about__title">Wer sind wir?</h2>
      <p class="about__text"><b>Frostwerk GmbH</b> ist Ihr zuverlässiger Partner im Bereich <b>Klima-, Wärmepumpen und Lüftungstechnik.</b></p>
      <p class="services">Installation | Verkauf | Wartung</p>
    </div>
    <div class="band band--front">frostwerk-klima.de</div>
  </section>

</main>
</body>
</html>
```